Business Card Design For A Renovation Contractor Company

We need a business card for a new company based in Singapore, our company name is "KT Planora". We are a renovation contractor that builds designs into reality. We build more of F&B restaurants, retail stores and commercial offices. We work very closely with designers. The final design should communicate to our client that we are a company that you can trust, that will plan and complete your project without giving you a headache. I like my client to remember my company as "KT". The beauty of SIMPLE is important.

Industry/Entity Type

Contractor

Requirements
Nice to have
• Black or Red base

```html
<!DOCTYPE html>
<html lang="en">
<head>
<meta charset="utf-8">
<title>KT Planora – Business Card</title>
<link href="https://fonts.googleapis.com/css2?family=Montserrat:wght@300;400;500;600&display=swap" rel="stylesheet">
<style>
  :root {
    --backdrop: #2a2a2a;
    --card-red: #e3061e;
    --card-red-deep: #c50017;
    --card-dark: #1c1a1d;
    --card-dark-edge: #141215;
    --accent-red: #e0101f;
    --text-light: #f2f2f2;
    --text-muted: #cfcfcf;
    --text-ink: #1a1a1a;
  }
  * { box-sizing: border-box; margin: 0; padding: 0; }
  html, body {
    width: 1200px; height: 901px; overflow: hidden;
    background: var(--backdrop);
    font-family: "Montserrat", sans-serif;
  }
  .stage {
    width: 1200px; height: 901px;
    display: flex; align-items: center; justify-content: center; gap: 40px;
  }
  .card {
    position: relative;
    width: 540px; height: 309px;
    box-shadow: 0 14px 30px rgba(0,0,0,.45);
    overflow: hidden;
  }
  /* Front */
  .card--front {
    background: linear-gradient(135deg, var(--card-red) 0%, var(--card-red-deep) 100%);
    display: flex; flex-direction: column; align-items: center; justify-content: center;
  }
  .brand { display: flex; align-items: center; gap: 14px; }
  .brand__dot {
    width: 46px; height: 46px; border-radius: 50%;
    border: 3px solid currentColor;
    flex: none;
  }
  .brand__name {
    font-weight: 400; font-size: 44px; letter-spacing: .5px; line-height: 1;
    white-space: nowrap;
  }
  .card--front .brand { color: var(--text-light); }
  .tagline {
    margin-top: 8px;
    font-weight: 400; font-size: 14px; letter-spacing: .6px;
    border-top: 1px solid currentColor; padding-top: 3px;
    white-space: nowrap;
  }
  .card--front .tagline { color: var(--text-ink); }
  .website {
    position: absolute; bottom: 26px; left: 0; right: 0; text-align: center;
    font-size: 11px; font-weight: 500; color: var(--text-ink); letter-spacing: .4px;
  }
  /* Back */
  .card--back {
    background: linear-gradient(135deg, var(--card-dark) 0%, var(--card-dark-edge) 100%);
    color: var(--text-light);
  }
  .card--back .brand-block {
    position: absolute; top: 34px; left: 0; right: 0;
    display: flex; flex-direction: column; align-items: center;
  }
  .card--back .brand__dot { width: 32px; height: 32px; border-width: 2px; border-color: var(--accent-red); }
  .card--back .brand__name { font-size: 32px; }
  .card--back .tagline { font-size: 11px; color: var(--text-muted); border-color: var(--text-muted); }
  .person { position: absolute; left: 34px; top: 168px; }
  .person__name { color: var(--accent-red); font-weight: 600; font-size: 17px; }
  .person__role { font-weight: 500; font-size: 12px; margin-top: 2px; }
  .contacts { position: absolute; left: 34px; top: 222px; font-size: 12px; line-height: 1.6; }
  .contacts dt { color: var(--accent-red); font-weight: 500; display: inline-block; width: 54px; }
  .contacts dd { display: inline; font-weight: 400; }
  .contacts dd::after { content: ""; display: block; }
  .address { position: absolute; right: 34px; top: 168px; font-size: 12px; line-height: 1.6; text-align: left; font-style: normal; }
  .address__label { color: var(--accent-red); font-weight: 500; }
</style>
</head>
<body>
<main class="stage">
  <section class="card card--front" aria-label="Card front">
    <div class="brand">
      <span class="brand__dot"></span>
      <span class="brand__name">KT Planora</span>
    </div>
    <p class="tagline">crafting spaces you can trust</p>
    <p class="website">www.ktplanora.com</p>
  </section>

  <section class="card card--back" aria-label="Card back">
    <div class="brand-block">
      <div class="brand">
        <span class="brand__dot"></span>
        <span class="brand__name">KT Planora</span>
      </div>
      <p class="tagline">crafting spaces you can trust</p>
    </div>
    <div class="person">
      <p class="person__name">Marcus Tan</p>
      <p class="person__role">Position Director</p>
    </div>
    <dl class="contacts">
      <dt>Phone</dt><dd>6123 456 789</dd>
      <dt>Cell</dt><dd>9876 543 210</dd>
      <dt>Email</dt><dd>marcus@ktplanora.com</dd>
    </dl>
    <address class="address">
      <span class="address__label">Address</span> 12 Keong Saik Lane<br>
      #03-208 Keong Saik Centre<br>
      Singapore 089123
    </address>
  </section>
</main>
</body>
</html>
```